Trade Show Display Design For A Real Estate Lending Company

We are in need of an impactful and modern trade show booth design that is consistent with the new branding and imagery found on our website www.qvt7.net.

Established in 2010, Crestmoor Funding Partners, LLC is a Hard Money Lender providing fast bridge financing to real estate investors for the purchase, renovation, or new construction of single family, multi-family and mixed use properties. We have closed over 800 loans since we began with total transaction amounts in excess of $170 million.

We like to stress that we are local lenders, and our lending area includes NJ, NY, CT, MA, PA, FL, MD, VA, DC. In addition, one of our major differentiators is that we close loans extremely fast.
Here is what we need for this project, and the artwork templates are attached.

-1 backdrop display design
-1 countertop wrap design
-1 retractable banner design

The backdrop display and the countertop will be used together. The retractable banner will be used together with the backdrop and by itself.

Target Market(s)

Real estate agents, mortgage brokers, builders, and other real estate investors.

Industry/Entity Type

Real Estate

Font styles to use
Other font styles liked:
• Proxima Nova and Roboto Slab (or similar)

Requirements
Must have
• Must include a design for all three elements (backdrop, retractable banner, counter top). Final submission must also be submitted using the print-ready art templates provided.

```html
<!DOCTYPE html>
<html lang="en">
<head>
<meta charset="utf-8">
<title>Crestmoor Funding Partners – Retractable Banner</title>
<link rel="stylesheet" href="https://fonts.googleapis.com/css2?family=Roboto+Condensed:wght@400;500;700&family=Roboto:wght@500;700&display=swap">
<style>
  :root{
    --bg:#f2f3f4;
    --teal:#1c5b6b;
    --teal-dark:#174b59;
    --green:#2f9a86;
    --orange:#e8862b;
    --ink:#1f4a5c;
    --white:#ffffff;
    --photo-a:#b8674c;
    --photo-b:#6f7f8c;
    --photo-c:#3a4d63;
  }
  *{box-sizing:border-box;margin:0;padding:0}
  html,body{width:1200px;height:1200px;overflow:hidden;background:var(--bg)}
  .canvas{position:relative;width:1200px;height:1200px}
  .banner{position:absolute;left:390px;top:30px;width:420px;height:1140px;background:var(--white);overflow:hidden;
    font-family:"Roboto Condensed",Arial,sans-serif;color:var(--ink)}
  .hero-photo{position:absolute;left:0;top:0;width:420px;height:680px;
    background:linear-gradient(170deg,var(--photo-a) 0%,#c98a6e 28%,var(--photo-b) 55%,var(--photo-c) 80%,#8a5a48 100%)}
  .shapes{position:absolute;left:0;top:0}
  .brand{position:absolute;right:26px;top:44px;width:210px;display:flex;align-items:center;gap:10px;
    font-family:"Roboto",Arial,sans-serif;font-weight:500;font-size:17px;line-height:1.15;color:var(--white);text-transform:uppercase}
  .brand-dot{flex:none;width:14px;height:14px;border-radius:50%;background:var(--white)}
  .tagline{position:absolute;left:0;width:420px;top:562px;text-align:center;color:var(--white);
    font-weight:700;font-size:21px;letter-spacing:.1px;text-shadow:0 1px 3px rgba(0,0,0,.45)}
  .section-title{position:absolute;left:0;width:420px;text-align:center;color:var(--orange);font-weight:700}
  .section-title svg{vertical-align:-3px;margin-right:10px}
  .deliver-title{top:700px;font-size:22px}
  .features{position:absolute;left:18px;top:740px;width:384px;display:grid;grid-template-columns:repeat(3,1fr);row-gap:22px}
  .feature{text-align:center;font-size:14.5px;font-weight:500;color:var(--ink)}
  .feature svg{display:block;margin:0 auto 8px}
  .states-title{top:945px;font-size:19px}
  .states{position:absolute;left:0;width:420px;top:978px;text-align:center;font-size:12.5px;font-weight:500;line-height:26px;color:var(--ink);text-transform:uppercase}
  .states span{padding:0 7px;border-left:1.5px solid var(--ink)}
  .states span:first-child{border-left:none}
  .contact-bar{position:absolute;left:20px;top:1060px;width:380px;height:21px;border-radius:11px;background:var(--teal);
    display:flex;justify-content:space-around;align-items:center;color:var(--white);font-size:11px}
  .contact-bar svg{vertical-align:-2px;margin-right:5px}
  .foot-band{position:absolute;left:0;bottom:0;width:420px;height:40px;background:var(--green)}
</style>
</head>
<body>
<div class="canvas">
  <div class="banner">
    <div class="hero-photo" role="img" aria-label="Photo of two smiling builders kneeling on a rooftop with clay tiles, a spirit level resting on a brick wall in front of them"></div>

    <svg class="shapes" width="420" height="1140" viewBox="0 0 420 1140" aria-hidden="true">
      <path d="M40,0 H420 V150 C330,175 210,120 110,70 C75,50 52,28 40,0Z" fill="var(--teal)"/>
      <path d="M110,70 C210,120 330,175 420,150" fill="none" stroke="var(--green)" stroke-width="5"/>
      <path d="M0,592 C110,640 250,595 420,590 V650 C260,640 120,670 0,700Z" fill="var(--teal)"/>
      <path d="M0,700 C120,670 260,640 420,650 V1140 H0Z" fill="var(--white)"/>
      <path d="M0,700 C120,670 260,640 420,650" fill="none" stroke="var(--green)" stroke-width="4"/>
    </svg>

    <div class="brand"><span class="brand-dot"></span><span>Crestmoor Funding Partners, LLC</span></div>

    <p class="tagline">Your Local Hard Money Lending Partner</p>

    <h2 class="section-title deliver-title">
      <svg width="20" height="20" viewBox="0 0 20 20"><circle cx="10" cy="10" r="4" fill="none" stroke="var(--orange)" stroke-width="1.6"/><g stroke="var(--orange)" stroke-width="1.6"><line x1="10" y1="1" x2="10" y2="3.5"/><line x1="10" y1="16.5" x2="10" y2="19"/><line x1="1" y1="10" x2="3.5" y2="10"/><line x1="16.5" y1="10" x2="19" y2="10"/><line x1="3.6" y1="3.6" x2="5.4" y2="5.4"/><line x1="14.6" y1="14.6" x2="16.4" y2="16.4"/><line x1="16.4" y1="3.6" x2="14.6" y2="5.4"/><line x1="5.4" y1="14.6" x2="3.6" y2="16.4"/></g></svg>We Deliver :
    </h2>

    <div class="features">
      <div class="feature">
        <svg width="34" height="34" viewBox="0 0 34 34" fill="none" stroke="var(--ink)" stroke-width="1.8"><circle cx="17" cy="17" r="14"/><path d="M21 12.5c-1-1.4-2.4-2-4-2-2.2 0-3.8 1.2-3.8 3s1.6 2.6 3.8 3.2 4 1.3 4 3.3-1.8 3.2-4 3.2c-1.8 0-3.3-.7-4.2-2.1M17 8v18"/></svg>
        Hard Money
      </div>
      <div class="feature">
        <svg width="34" height="34" viewBox="0 0 34 34" fill="none" stroke="var(--ink)" stroke-width="1.8"><circle cx="17" cy="17" r="14"/><circle cx="17" cy="17" r="10"/><path d="M17 17l5-5"/><circle cx="17" cy="17" r="1.5" fill="var(--ink)"/></svg>
        Fast Processing
      </div>
      <div class="feature">
        <svg width="34" height="34" viewBox="0 0 34 34" fill="none" stroke="var(--ink)" stroke-width="1.8"><circle cx="17" cy="17" r="14"/><ellipse cx="17" cy="17" rx="6" ry="14"/><path d="M3 17h28M6 10h22M6 24h22"/></svg>
        Local Services
      </div>
      <div class="feature">
        <svg width="34" height="34" viewBox="0 0 34 34" fill="none" stroke="var(--ink)" stroke-width="1.8"><path d="M5 8h20a3 3 0 0 1 3 3v10a3 3 0 0 1-3 3H13l-6 5v-5H5a3 3 0 0 1-3-3V11a3 3 0 0 1 3-3z"/><circle cx="10" cy="16" r="1.2" fill="var(--ink)"/><circle cx="15" cy="16" r="1.2" fill="var(--ink)"/><circle cx="20" cy="16" r="1.2" fill="var(--ink)"/></svg>
        Financial Coaching
      </div>
      <div class="feature">
        <svg width="34" height="34" viewBox="0 0 34 34" fill="none" stroke="var(--ink)" stroke-width="1.8"><path d="M4 30h26"/><rect x="6" y="20" width="4" height="10"/><rect x="13" y="15" width="4" height="15"/><rect x="20" y="18" width="4" height="12"/><rect x="27" y="10" width="3" height="20"/><path d="M5 14l8-6 7 4 9-8M25 4h4v4"/></svg>
        Profitability
      </div>
      <div class="feature">
        <svg width="34" height="34" viewBox="0 0 34 34" fill="none" stroke="var(--ink)" stroke-width="1.8"><circle cx="17" cy="17" r="14"/><path d="M11 17.5l4 4 8-9"/></svg>
        Peace of Mind
      </div>
    </div>

    <h2 class="section-title states-title">
      <svg width="18" height="18" viewBox="0 0 20 20"><circle cx="10" cy="10" r="4" fill="none" stroke="var(--orange)" stroke-width="1.6"/><g stroke="var(--orange)" stroke-width="1.6"><line x1="10" y1="1" x2="10" y2="3.5"/><line x1="10" y1="16.5" x2="10" y2="19"/><line x1="1" y1="10" x2="3.5" y2="10"/><line x1="16.5" y1="10" x2="19" y2="10"/></g></svg>CFP Lends In The Following States:
    </h2>

    <div class="states">
      <div><span>Connecticut</span><span>Florida</span><span>Maryland</span><span>Massachusetts</span></div>
      <div><span>New Jersey</span><span>New York</span><span>Pennsylvania</span><span>Virginia &amp; D.C.</span></div>
    </div>

    <div class="contact-bar">
      <span><svg width="10" height="10" viewBox="0 0 10 10"><rect x="2" y="0.5" width="6" height="9" rx="1" fill="none" stroke="var(--white)" stroke-width="1"/></svg>555.304.7712</span>
      <span><svg width="10" height="10" viewBox="0 0 10 10"><circle cx="5" cy="5" r="4" fill="none" stroke="var(--white)" stroke-width="1"/></svg>info@qvt7.net</span>
      <span><svg width="10" height="10" viewBox="0 0 10 10"><circle cx="5" cy="5" r="4" fill="var(--white)"/></svg>www.qvt7.net</span>
    </div>

    <div class="foot-band"></div>
  </div>
</div>
</body>
</html>
```